Bright Oak Fitness Facility Business Cards

Business Card Design that incorporates the logo and tagline

Target Market(s)

Fitness, People Who Exercise

Contact Information for Business Card

2817 Mossgrove Bend Road
Tavares, Florida 32190
Phone: 352-555-Jump (5867)
www.brightoakfitness.example
info@brightoakfitness.example

Requirements
Must have
• Logo, Address, Website, email and tagline "More Than A Gym". Colors should be red/black/grey/white

```html
<!DOCTYPE html>
<html lang="en">
<head>
<meta charset="utf-8">
<title>Bright Oak Fitness – Business Card</title>
<link rel="stylesheet" href="https://fonts.googleapis.com/css2?family=Montserrat:wght@400;500;700&display=swap">
<style>
  :root {
    --backdrop: #e9e6e2;
    --card-white: #ffffff;
    --brand-red: #ec1c24;
    --ink-black: #1b1b1b;
    --text-grey: #3a3a3a;
    --rule-grey: #9a9a9a;
  }
  * { box-sizing: border-box; margin: 0; padding: 0; }
  html, body {
    width: 1200px; height: 950px; overflow: hidden;
    background: var(--backdrop);
    font-family: "Montserrat", sans-serif;
  }
  .stage {
    width: 1200px; height: 950px;
    display: flex; align-items: center; justify-content: center;
  }
  .business-card {
    position: relative;
    width: 1000px; height: 580px;
    background: var(--card-white);
    border-radius: 28px;
    overflow: hidden;
    box-shadow: 0 10px 30px rgba(0,0,0,0.18);
  }
  .card-wave {
    position: absolute; inset: 0;
    width: 1000px; height: 580px;
  }
  .brand-lockup {
    position: absolute; left: 150px; top: 120px;
    display: flex; align-items: center; gap: 16px;
  }
  .brand-mark {
    width: 34px; height: 34px;
    background: var(--brand-red);
  }
  .brand-name {
    font-weight: 700; font-size: 44px; letter-spacing: 1px;
    color: var(--ink-black);
    text-transform: uppercase;
  }
  .brand-rule {
    position: absolute; left: 150px; top: 192px;
    width: 330px; height: 3px; background: var(--rule-grey);
  }
  .person-name {
    position: absolute; left: 270px; top: 232px;
    font-size: 34px; font-weight: 400; letter-spacing: 1px;
    color: var(--brand-red); text-transform: uppercase;
  }
  .person-title {
    position: absolute; left: 272px; top: 280px;
    font-size: 20px; font-weight: 500; letter-spacing: 0.5px;
    color: var(--ink-black); text-transform: uppercase;
  }
  .contact-block {
    position: absolute; left: 60px; top: 380px;
    font-size: 14px; font-weight: 400; color: var(--text-grey);
    line-height: 32px; white-space: nowrap;
  }
  .contact-label { color: var(--brand-red); }
  .tagline {
    position: absolute; left: 650px; bottom: 22px;
    font-size: 18px; font-weight: 500; color: var(--card-white);
  }
</style>
</head>
<body>
<main class="stage">
  <section class="business-card">
    <svg class="card-wave" viewBox="0 0 1000 580" aria-hidden="true">
      <path d="M850 0 C930 40 910 200 840 330 C770 450 680 540 560 580 L1000 580 L1000 0 Z" fill="var(--ink-black)"/>
      <path d="M872 0 C952 40 932 200 862 330 C792 450 702 540 584 580 L1000 580 L1000 0 Z" fill="var(--brand-red)"/>
    </svg>

    <div class="brand-lockup">
      <span class="brand-mark"></span>
      <span class="brand-name">Bright Oak Fitness</span>
    </div>
    <div class="brand-rule"></div>

    <h1 class="person-name">Dana Whitfield</h1>
    <p class="person-title">CEO/Founder</p>

    <div class="contact-block">
      <p class="contact-address">2817 Mossgrove Bend Road Tavares, Florida 32190</p>
      <p class="contact-lines">
        <span class="contact-label">P:</span> 352-555-5867
        <span class="contact-label">E:</span> info@brightoakfitness.example
        <span class="contact-label">W:</span> www.brightoakfitness.example
      </p>
    </div>

    <p class="tagline">More Than A Gym</p>
  </section>
</main>
</body>
</html>
```